Facebook Ad for Black Friday 25% off Sitewide

Hi I need a really good FB/Instagram Ad for Black Friday using the pictures of our jackets in our store. Should be size best for FB and Instagram which is 1200 x 628.Our jackets are our #1 selling product in our store. Yellow being #1 best selling and Black is the #2 Best Selling.

Black Friday Sale Promotion-25% off our entire website-Friday Only

Target Market(s)

Girls age 18-35

Industry/Entity Type

Fashion

Requirements
Must have
• Black Background, jackets displayed nicely maybe with some peace signs like my logo or whatever you think would make a good black friday ad.
Nice to have
• Something that really pops
Should not have
• Boring

```html
<!DOCTYPE html>
<html lang="en">
<head>
<meta charset="utf-8">
<title>Black Friday Sale – 25% Off Sitewide</title>
<link rel="stylesheet" href="https://fonts.googleapis.com/css2?family=Roboto:wght@400;700;900&display=swap">
<style>
  :root {
    --bg: #484848;
    --yellow: #fff200;
    --black: #0b0b0b;
    --white: #ffffff;
    --jacket-yellow-1: #f2e53a;
    --jacket-yellow-2: #c9b81c;
    --jacket-black-1: #3a3a3a;
    --jacket-black-2: #151515;
    --fur: #b9ada0;
  }
  html, body {
    margin: 0;
    padding: 0;
    overflow: hidden;
    background: var(--bg);
  }
  .ad {
    position: relative;
    width: 1200px;
    height: 628px;
    background: var(--bg);
    overflow: hidden;
    font-family: "Roboto", Arial, sans-serif;
  }
  .ad svg { display: block; }
  .headline-text { font-weight: 700; fill: var(--yellow); }
  .sale-word { font-weight: 700; fill: var(--yellow); letter-spacing: 10px; }
  .discount-number { font-weight: 900; fill: var(--yellow); letter-spacing: -4px; }
  .discount-sign { font-weight: 900; fill: var(--yellow); }
  .offer-line { font-weight: 400; fill: var(--white); }
  .offer-highlight { fill: var(--yellow); }
  .coupon-line { font-weight: 700; fill: var(--yellow); }
  .coupon-code { fill: var(--white); }
</style>
</head>
<body>
<div class="ad">
  <svg width="1200" height="628" viewBox="0 0 1200 628" xmlns="http://www.w3.org/2000/svg">
    <defs>
      <linearGradient id="yellowJacket" x1="0" y1="0" x2="1" y2="1">
        <stop offset="0" stop-color="var(--fur)"/>
        <stop offset="0.3" stop-color="var(--jacket-yellow-1)"/>
        <stop offset="1" stop-color="var(--jacket-yellow-2)"/>
      </linearGradient>
      <linearGradient id="blackJacket" x1="0" y1="0" x2="0" y2="1">
        <stop offset="0" stop-color="var(--fur)"/>
        <stop offset="0.4" stop-color="var(--jacket-black-1)"/>
        <stop offset="1" stop-color="var(--jacket-black-2)"/>
      </linearGradient>
      <linearGradient id="mintJacket" x1="0" y1="0" x2="0" y2="1">
        <stop offset="0" stop-color="#d8d2c8"/>
        <stop offset="1" stop-color="#9fe3e6"/>
      </linearGradient>
      <linearGradient id="coralJacket" x1="0" y1="0" x2="0" y2="1">
        <stop offset="0" stop-color="#d8d2c8"/>
        <stop offset="1" stop-color="#f0655a"/>
      </linearGradient>
      <linearGradient id="navyJacket" x1="0" y1="0" x2="0" y2="1">
        <stop offset="0" stop-color="#d8d2c8"/>
        <stop offset="1" stop-color="#2c3f93"/>
      </linearGradient>
    </defs>

    <!-- Featured jackets -->
    <path class="jacket-photo jacket-yellow" role="img" aria-label="Yellow puffer jacket with fur-trimmed knit hood"
          d="M0 0 H170 Q200 120 190 260 Q215 420 210 628 H0 Z" fill="url(#yellowJacket)"/>
    <path class="jacket-photo jacket-black" role="img" aria-label="Black puffer jacket with fur-trimmed knit hood"
          d="M1200 0 H1080 Q1010 80 1020 200 Q1000 400 990 628 H1200 Z" fill="url(#blackJacket)"/>

    <!-- Sale tag -->
    <g class="sale-tag">
      <polygon points="490,186 553,93 988,93 988,280 553,280" fill="var(--black)" stroke="var(--yellow)" stroke-width="4" stroke-linejoin="miter"/>
      <circle cx="527" cy="184" r="15" fill="none" stroke="var(--yellow)" stroke-width="3"/>
      <path class="tag-string" d="M520 190 C500 230 525 260 555 300 C585 340 615 380 605 392 C590 402 560 360 575 330 C590 300 540 240 536 190"
            fill="none" stroke="var(--white)" stroke-width="2.5" stroke-linecap="round"/>
      <text class="headline-text" x="585" y="149" font-size="35">BLACK FRIDAY</text>
      <text class="sale-word" x="583" y="245" font-size="104">SALE!</text>
    </g>

    <!-- Discount -->
    <g class="discount">
      <text class="discount-number" x="238" y="222" font-size="128">25</text>
      <text class="discount-sign" x="390" y="172" font-size="50">%</text>
      <text class="discount-sign" x="388" y="220" font-size="58">off</text>
      <text class="offer-line" x="240" y="246" font-size="18">Sitewide - <tspan class="offer-highlight">FRIDAY</tspan> only!</text>
      <text class="coupon-line" x="240" y="271" font-size="21">COUPON CODE: <tspan class="coupon-code">BLACK</tspan></text>
    </g>

    <!-- Colour options -->
    <g class="colour-options">
      <circle cx="447" cy="481" r="66" fill="var(--yellow)"/>
      <circle cx="447" cy="481" r="61" fill="var(--white)"/>
      <circle cx="447" cy="481" r="58" fill="url(#mintJacket)" role="img" aria-label="Mint puffer jacket with fur hood"/>

      <circle cx="607" cy="481" r="66" fill="var(--yellow)"/>
      <circle cx="607" cy="481" r="61" fill="var(--white)"/>
      <circle cx="607" cy="481" r="58" fill="url(#coralJacket)" role="img" aria-label="Coral puffer jacket with fur hood"/>

      <circle cx="767" cy="481" r="66" fill="var(--yellow)"/>
      <circle cx="767" cy="481" r="61" fill="var(--white)"/>
      <circle cx="767" cy="481" r="58" fill="url(#navyJacket)" role="img" aria-label="Navy puffer jacket with fur hood"/>
    </g>
  </svg>
</div>
</body>
</html>
```